Copper Kettle Catering Menu

Design 1 page (double sided is ok) menu for catering company.

A flat non-folding menu. Letter paper sized.
Updates

I'm having trouble adding attachments via Drafting Hive.  I have contacted Drafting Hive and will hopefully have them up soon.  

Industry/Entity Type

Catering

Font styles to use
Serif

Requirements
Must have
• Copper Kettle Catering logo

menu items from attachment

Double sided is ok

```html
<!DOCTYPE html>
<html lang="en">
<head>
<meta charset="utf-8">
<title>Copper Kettle Catering – Food Menu</title>
<link rel="stylesheet" href="https://fonts.googleapis.com/css2?family=Cinzel:wght@400;700&family=Arimo:wght@400&display=swap">
<style>
  :root {
    --sky-top: #6fd3f2;
    --sky-mid: #35c0ee;
    --sky-bottom: #18ace3;
    --sky-glow: rgba(220, 245, 252, 0.85);
    --brand-blue: #1d4f9c;
    --card-white: #ffffff;
    --card-edge: #8a9aa5;
    --white: #ffffff;
    --faint-white: rgba(255, 255, 255, 0.28);
    --lime: #d5e021;
    --lime-edge: #c3ce17;
    --ink-navy: #1b2456;
    --wine: #b5335f;
  }
  * { box-sizing: border-box; margin: 0; padding: 0; }
  html, body { width: 927px; height: 1200px; overflow: hidden; }
  body { font-family: "Cinzel", "Times New Roman", serif; }

  .menu-page {
    position: relative;
    width: 927px;
    height: 1200px;
    overflow: hidden;
    background:
      radial-gradient(ellipse 420px 300px at 470px 320px, var(--sky-glow), rgba(220,245,252,0) 100%),
      linear-gradient(180deg, var(--sky-top) 0%, var(--sky-mid) 45%, var(--sky-bottom) 100%);
  }

  .sky-scene {
    position: absolute; inset: 0;
    background:
      radial-gradient(ellipse 120px 18px at 80px 120px, rgba(255,255,255,0.55), transparent),
      radial-gradient(ellipse 140px 20px at 850px 40px, rgba(255,255,255,0.55), transparent),
      radial-gradient(ellipse 130px 18px at 860px 230px, rgba(255,255,255,0.5), transparent),
      radial-gradient(ellipse 160px 22px at 110px 360px, rgba(255,255,255,0.35), transparent),
      radial-gradient(ellipse 180px 24px at 820px 400px, rgba(255,255,255,0.35), transparent);
  }

  .brand-card {
    position: absolute;
    left: 124px; top: 71px;
    width: 684px; height: 191px;
    background: var(--card-white);
    border: 2px solid var(--card-edge);
    border-radius: 14px;
    box-shadow: 0 2px 6px rgba(0,0,0,0.2);
    display: flex; flex-direction: column; align-items: center; justify-content: center;
    color: var(--brand-blue);
    font-weight: 400;
  }
  .brand-card .brand-small { font-size: 20px; letter-spacing: 14px; }
  .brand-card .brand-name { font-size: 44px; letter-spacing: 1px; margin: 12px 0; }

  .side-name {
    position: absolute;
    left: 130px; top: 690px;
    width: 620px;
    transform: translate(-50%, -50%) rotate(-90deg);
    text-align: center;
    color: var(--faint-white);
    font-size: 46px;
    white-space: nowrap;
  }

  .menu-title {
    position: absolute;
    left: 273px; top: 484px;
    width: 370px;
    color: var(--white);
    font-family: "Arimo", Arial, sans-serif;
    font-size: 26px;
    letter-spacing: 14px;
    text-align: center;
  }

  .cutlery-art {
    position: absolute;
    left: 258px; top: 530px;
    width: 440px; height: 205px;
    background: radial-gradient(ellipse at center, rgba(255,255,255,0.22), rgba(255,255,255,0.04) 75%);
    border-radius: 40px;
  }

  .occasions {
    position: absolute;
    left: 180px; top: 772px;
    width: 560px;
    text-align: center;
    color: var(--white);
  }
  .occasions h2 { font-size: 27px; font-weight: 400; line-height: 1.1; }
  .occasions p { font-size: 19px; line-height: 26px; margin-top: 2px; }

  .celebration-art {
    position: absolute;
    left: 712px; top: 720px;
    width: 174px; height: 220px;
    background: linear-gradient(160deg, rgba(240,240,80,0.55), rgba(255,255,255,0.35) 45%, rgba(181,51,95,0.7) 100%);
    border-radius: 30px;
  }

  .menu-tab {
    position: absolute;
    background: var(--lime);
    border: 1px solid var(--lime-edge);
    color: var(--ink-navy);
    font-size: 25px;
    display: flex; align-items: center; justify-content: center;
    white-space: nowrap;
  }
  .tab-breakfast { left: 223px; top: 947px; width: 194px; height: 49px; }
  .tab-lunch     { left: 447px; top: 947px; width: 195px; height: 49px; }
  .tab-sandwich  { left: 671px; top: 947px; width: 191px; height: 49px; }
  .tab-salads    { left: 223px; top: 1006px; width: 130px; height: 50px; }
  .tab-buffets   { left: 377px; top: 1006px; width: 312px; height: 50px; }
  .tab-snacks    { left: 709px; top: 1006px; width: 153px; height: 50px; }

  .help-box {
    position: absolute;
    left: 42px; top: 1017px;
    width: 169px; height: 127px;
    background: var(--lime);
    border: 1px solid var(--lime-edge);
    color: var(--ink-navy);
    font-family: "Arimo", Arial, sans-serif;
    font-size: 24px;
    line-height: 28px;
    display: flex; align-items: center; justify-content: center;
    text-align: center;
  }

  .contact-band {
    position: absolute;
    left: 223px; top: 1066px;
    width: 704px; height: 76px;
    background: var(--lime);
    color: var(--ink-navy);
    padding: 16px 0 0 50px;
    font-size: 17px;
    line-height: 22px;
    white-space: nowrap;
  }
</style>
</head>
<body>
<main class="menu-page">
  <div class="sky-scene" role="img" aria-label="Bright blue sky with soft white clouds"></div>

  <header class="brand-card">
    <span class="brand-small">The</span>
    <span class="brand-name">Copper Kettle Catering</span>
    <span class="brand-small">Company</span>
  </header>

  <div class="side-name" aria-hidden="true">Copper Kettle Catering</div>

  <h1 class="menu-title">Food Menu</h1>
  <div class="cutlery-art" role="img" aria-label="Sketched fork, plate, knife and spoon in white line drawing"></div>

  <section class="occasions">
    <h2>Caterings for all Occasions</h2>
    <p>Enjoy our pre-set menu or we can<br>customize something more personal.<br>Set up and delivery is included in all<br>prices listed.</p>
  </section>

  <div class="celebration-art" role="img" aria-label="Starfish with a wine bottle and glass"></div>

  <nav>
    <div class="menu-tab tab-breakfast">Breakfast</div>
    <div class="menu-tab tab-lunch">Lunch</div>
    <div class="menu-tab tab-sandwich">Sandwich</div>
    <div class="menu-tab tab-salads">Salads</div>
    <div class="menu-tab tab-buffets">Hot Lunch Buffets</div>
    <div class="menu-tab tab-snacks">Snacks</div>
  </nav>

  <div class="help-box">WE<br>ARE HERE<br>TO HELP</div>

  <footer class="contact-band">
    Catering Director: Dana Whitlock<br>
    Phone: 555-014-3905 | Fax: 555-014-1939 &nbsp;| Cell: 555-019-0141
  </footer>
</main>
</body>
</html>
```